Business cards — need something that creates “wow” factor

Need a sleek and clean looking business card. Something that is clear and consise. These business cards are for my painting business and hundreds will be placed in the Dallas area between all Halverd Pemberton paint stored. These card really need to stick out! Open to any and all ideas...

Target Market(s)

Residential clientele

Industry/Entity Type

Painting

Contact Information for Business Card

Dorian Vakelby
Owner

382.516.2074

Web: Mesahuepainting.example (still under construction)
Mesahuepainting@mailbox.example

Font styles to use
Sans Serif

Colors

Designer to choose colors to be used in the design.

Requirements
Must have
• My name, number, website, email, Socialpage
• and “100% customer satisfaction guaranteed”
• Socialpage.example/Mesahuepainting/
Nice to have
• Listed services
• Interior/exterior painting
• Drywall repair/texture
• Fence staining/refinishing
• Concrete staining
• Epoxy flooring
• Pressure washing

```html
<!DOCTYPE html>
<html lang="en">
<head>
<meta charset="utf-8">
<title>Mesahue Painting – Business Card</title>
<link rel="stylesheet" href="https://fonts.googleapis.com/css2?family=Roboto:ital,wght@0,300;0,400;0,500;1,700&display=swap">
<style>
  :root {
    --canvas: #e9e7e4;
    --card-black: #050505;
    --card-white: #f3f3f3;
    --ink-dark: #1d1d1d;
    --ink-light: #f4f4f4;
    --accent-teal: #3a93b4;
    --band-red: #b3202c;
    --band-orange: #f08a1c;
    --band-lime: #9ccf5c;
    --band-teal: #3a93b4;
    --dot-red: #b3262d;
    --dot-coral: #e2452b;
    --dot-orange: #f08a1f;
    --dot-green: #6cc24a;
    --dot-teal: #2f98b8;
    --dot-purple: #8a4a9a;
    --muted: #7a7a7a;
  }
  * { margin: 0; padding: 0; box-sizing: border-box; }
  html, body { width: 1200px; height: 960px; overflow: hidden; }
  body {
    background: var(--canvas);
    font-family: "Roboto", Arial, sans-serif;
    position: relative;
  }
  .card {
    position: absolute;
    width: 600px;
    height: 343px;
    background: var(--card-black);
    overflow: hidden;
  }
  .card--front { left: 314px; top: 113px; }
  .card--back { left: 311px; top: 472px; }

  .brand-panel {
    position: absolute;
    left: 0; top: 0;
    width: 298px; height: 343px;
    background: var(--card-white);
  }
  .brand-name {
    position: absolute;
    left: 0; width: 298px; top: 128px;
    text-align: center;
    font-size: 42px;
    font-weight: 400;
    letter-spacing: 2px;
    color: var(--ink-dark);
  }
  .brand-tagline {
    position: absolute;
    left: 0; width: 298px; top: 198px;
    text-align: center;
    font-size: 7.5px;
    font-weight: 300;
    color: var(--muted);
  }

  .contact-block {
    position: absolute;
    left: 334px; top: 89px;
    color: var(--ink-light);
  }
  .contact-name {
    font-size: 20px;
    font-weight: 500;
    color: var(--accent-teal);
    text-transform: uppercase;
    letter-spacing: 0.3px;
    line-height: 24px;
  }
  .contact-role {
    font-size: 15px;
    font-weight: 400;
    text-transform: uppercase;
    line-height: 20px;
  }
  .contact-list {
    list-style: none;
    margin-top: 18px;
  }
  .contact-list li {
    display: flex;
    align-items: center;
    height: 19.3px;
    font-size: 14.5px;
  }
  .contact-list svg {
    width: 13px; height: 13px;
    margin-right: 9px;
    fill: var(--accent-teal);
    flex: none;
  }

  .promise-band {
    position: absolute;
    left: 0; top: 291px;
    width: 600px; height: 32px;
    background: linear-gradient(90deg, var(--band-red) 0%, #e23a2a 30%, var(--band-orange) 55%, var(--band-lime) 78%, var(--band-teal) 100%);
    display: flex; align-items: center; justify-content: center;
  }
  .promise-text {
    font-size: 16px;
    font-weight: 700;
    font-style: italic;
    color: #141414;
  }

  .services {
    list-style: none;
    position: absolute;
    left: 0; top: 68px; width: 600px;
    text-align: center;
    color: var(--ink-light);
  }
  .services li {
    font-size: 21px;
    font-weight: 400;
    line-height: 34px;
  }
  .services li::before {
    content: "";
    display: inline-block;
    width: 8px; height: 8px;
    border-radius: 50%;
    margin-right: 9px;
    vertical-align: middle;
    position: relative; top: -2px;
    background: var(--dot, #fff);
  }
  .service--red { --dot: var(--dot-red); }
  .service--coral { --dot: var(--dot-coral); }
  .service--orange { --dot: var(--dot-orange); }
  .service--green { --dot: var(--dot-green); }
  .service--teal { --dot: var(--dot-teal); }
  .service--purple { --dot: var(--dot-purple); }
</style>
</head>
<body>

<section class="card card--front">
  <div class="brand-panel">
    <div class="brand-name">MESAHUE</div>
    <div class="brand-tagline">Commercial | Residential | Interior | Exterior</div>
  </div>

  <div class="contact-block">
    <div class="contact-name">Dorian Vakelby</div>
    <div class="contact-role">Owner</div>
    <ul class="contact-list">
      <li>
        <svg viewBox="0 0 24 24" aria-hidden="true"><path d="M6.6 10.8a15.1 15.1 0 0 0 6.6 6.6l2.2-2.2c.3-.3.7-.4 1-.2 1.1.4 2.3.6 3.6.6.6 0 1 .4 1 1V20c0 .6-.4 1-1 1C10.6 21 3 13.4 3 4c0-.6.4-1 1-1h3.5c.6 0 1 .4 1 1 0 1.3.2 2.5.6 3.6.1.3 0 .7-.2 1L6.6 10.8z"/></svg>
        382.516.2074
      </li>
      <li>
        <svg viewBox="0 0 24 24" aria-hidden="true"><path d="M2 5h20v14H2z M2 5l10 8 10-8" /><path d="M3 6l9 7 9-7v-.5H3z" fill="#050505"/></svg>
        Mesahuepainting@mailbox.example
      </li>
      <li>
        <svg viewBox="0 0 24 24" aria-hidden="true"><circle cx="12" cy="12" r="10"/><path d="M2 12h20M12 2c3 3 3 17 0 20M12 2c-3 3-3 17 0 20" stroke="#050505" stroke-width="1.6" fill="none"/></svg>
        Mesahuepainting.example
      </li>
      <li>
        <svg viewBox="0 0 24 24" aria-hidden="true"><rect x="2" y="2" width="20" height="20" rx="2"/></svg>
        Mesahuepainting
      </li>
    </ul>
  </div>

  <div class="promise-band">
    <span class="promise-text">100% customer satisfaction guaranteed</span>
  </div>
</section>

<section class="card card--back">
  <ul class="services">
    <li class="service--red">Interior/exterior painting</li>
    <li class="service--coral">Drywall repair/texture</li>
    <li class="service--orange">Fence staining/refinishing</li>
    <li class="service--green">Concrete staining</li>
    <li class="service--teal">Epoxy flooring</li>
    <li class="service--purple">Pressure washing</li>
  </ul>
</section>

</body>
</html>
```